Website design for dressage horse training business

Looking to develop a new website design for a dressage horse training website. We want to change from a single landing page to one with multiple pages.
You are free to use your creativity to design the main landing page. This is the only page you need to design at this point. I would encourage looking at other Dressage Training websites to get a feel for what is typically on them. A few websites are listed below although I think the design of them could be better.
Notes:
- Menu to include: Home, Services, News Room, Blog, About Us, Contact,
- FAQ section on main page
- Logo to remain the same - the logo attached is not the correct color so change to match existing color.
- Change 'Sponsors' to 'Partnerships' on main page
Here is the link to the current site:
https://lindenridgestables.com/
Example sites
https://www.crestwoodsporthorsesco.com/
https://corinnalavelledressage.com/
Target Market(s)
Older women with disposable income
Number of Pages Required
1 page
Look and feel
Each slider illustrates characteristics of the customer's brand and the style your logo design should communicate.

```html
<!DOCTYPE html>
<html lang="en">
<head>
<meta charset="utf-8">
<title>Linden Ridge Stables</title>
<link href="https://fonts.googleapis.com/css2?family=Cinzel:wght@400;500;700&family=Open+Sans:wght@400;600;700&display=swap" rel="stylesheet">
<style>
:root{
  --bg:#262626;
  --bg-deep:#1b1b1b;
  --gold:#c9a27a;
  --white:#ffffff;
  --card:#ffffff;
  --ink:#3a3a3a;
  --line:#8a7a68;
}
*{box-sizing:border-box;margin:0;padding:0}
html,body{width:1200px;height:3253px;overflow:hidden}
body{background:var(--bg);font-family:"Open Sans",Arial,sans-serif;color:var(--white);position:relative}

/* nav */
.nav{position:absolute;left:0;top:0;width:1200px;height:51px;background:var(--bg);border-bottom:2px solid var(--gold);z-index:5}
.nav a{position:absolute;top:16px;font-size:16px;color:var(--gold);text-decoration:none;letter-spacing:.3px}
.nav a.active{border-bottom:3px solid var(--gold);padding-bottom:8px}
.brand{position:absolute;left:510px;top:-2px;width:198px;height:78px;background:var(--bg);border:2px solid var(--gold);border-top:none;border-radius:0 0 14px 14px;z-index:6;display:flex;align-items:center;justify-content:center;font-family:"Cinzel",Georgia,serif;font-size:22px;color:var(--gold);text-align:center;line-height:1.05}
.socials{position:absolute;display:flex;gap:11px}
.socials span{display:block;width:26px;height:26px;border-radius:6px;background:var(--gold)}

/* hero */
.hero{position:absolute;left:0;top:51px;width:1200px;height:560px;background:radial-gradient(ellipse at 35% 45%,#5e5e5e 0%,#474747 40%,#2f2f2f 100%)}
.hero-curve{position:absolute;left:0;top:480px}
.emblem{position:absolute;left:534px;top:69px;width:132px;height:132px;border-radius:50%;background:var(--gold)}
.rule{position:absolute;left:362px;width:478px;height:2px;background:var(--gold)}
.hero-title{position:absolute;left:200px;top:268px;width:800px;text-align:center;font-family:"Cinzel",Georgia,serif;font-size:48px;line-height:51px;color:var(--white);text-shadow:0 2px 8px rgba(0,0,0,.6)}
.hero-sub{position:absolute;left:200px;top:440px;width:800px;text-align:center;font-family:"Cinzel",Georgia,serif;font-size:20px;color:var(--gold)}
.ph-note{position:absolute;left:176px;top:426px;width:86px;text-align:center;font-size:10px;line-height:12px;color:#ddd}
.btn{position:absolute;height:34px;border:2px solid var(--gold);border-radius:18px;color:var(--gold);font-family:"Cinzel",Georgia,serif;font-size:17px;display:flex;align-items:center;justify-content:center}
.btn.lg{height:38px;font-size:22px;border-radius:20px}

/* sections */
.sec-title{position:absolute;text-align:center;font-family:"Cinzel",Georgia,serif;color:var(--gold);font-size:29px;font-weight:400}
.sec-head{position:absolute;left:178px;width:842px;display:flex;align-items:center;justify-content:center;gap:10px;font-family:"Cinzel",Georgia,serif;color:var(--gold);font-size:29px;font-weight:400}
.sec-head i{display:block;width:24px;height:34px;border-radius:50%;background:var(--gold)}
.dash{position:absolute;left:178px;width:842px;border-top:1px dashed var(--gold)}
.photo{position:absolute;border-radius:14px}
.photo-label{position:absolute;left:0;right:0;bottom:12px;text-align:center;font-weight:700;font-size:24px;color:rgba(255,255,255,.9)}
.blurb{position:absolute;text-align:center;font-size:14px;line-height:17px;color:var(--white)}
.bio{position:absolute;left:572px;top:1133px;width:411px;font-size:13.6px;line-height:16.85px;letter-spacing:-.15px;text-align:justify;color:var(--white)}

/* partners */
.partner{position:absolute;top:1609px;width:392px;height:414px;background:var(--card);border:2px solid var(--gold);border-radius:8px;color:var(--ink)}
.partner .mark{position:absolute;left:0;right:0;top:62px;display:flex;align-items:center;justify-content:center;gap:10px;font-family:"Open Sans",Arial,sans-serif;font-weight:700;font-size:26px}
.partner .mark b{display:block;width:22px;height:22px;border-radius:50%}
.partner h3{position:absolute;left:0;right:0;top:154px;text-align:center;font-family:"Cinzel",Georgia,serif;font-weight:500;font-size:22px;color:#222}
.partner p{position:absolute;left:30px;right:30px;top:192px;font-size:13.6px;line-height:16.9px;text-align:justify}
.partner .btn{top:366px;width:160px;height:30px;font-size:16px}

/* faq */
.faq{position:absolute;left:178px;top:2123px;width:842px}
.faq .q{height:34px;border-top:1px solid var(--line);display:flex;align-items:center;justify-content:space-between;padding:0 10px 0 18px;font-size:14px}
.faq .tri{width:0;height:0;border-left:10px solid transparent;border-right:10px solid transparent;border-top:15px solid var(--gold)}
.faq .tri.up{border-top:none;border-bottom:15px solid var(--gold)}
.faq .a{padding:6px 14px 26px 50px;font-size:14px;line-height:17px}
.more{position:absolute;left:178px;top:2634px;width:842px;text-align:center;font-size:14px;color:var(--gold)}

.map{position:absolute;left:196px;top:2685px;width:804px;height:322px;border-radius:8px;background:linear-gradient(135deg,#cfe3c4,#b9d4ae 60%,#d6e2cf)}

/* footer */
.footer{position:absolute;left:0;top:3049px;width:1200px;height:204px;background:var(--bg-deep)}
.contact-h{position:absolute;left:436px;top:48px;font-weight:700;font-size:16px}
.contact-t{position:absolute;left:436px;top:66px;width:520px;font-size:16px;line-height:19px;color:var(--gold)}
.phone{position:absolute;left:436px;top:125px;font-size:27px;font-weight:700}
.phone b{color:var(--gold)}
.copy{position:absolute;left:0;width:1200px;top:172px;text-align:center;font-size:10px;color:var(--gold)}
</style>
</head>
<body>

<nav class="nav">
  <a class="active" style="left:220px">HOME</a>
  <a style="left:289px">SERVICES</a>
  <a style="left:383px">NEWS ROOM</a>
  <a style="left:732px">BLOG</a>
  <a style="left:795px">ABOUT US</a>
  <a style="left:893px">CONTACT</a>
  <div class="socials" style="left:1081px;top:13px" aria-label="Social links"><span></span><span></span><span></span></div>
</nav>
<div class="brand">LINDEN<br>RIDGE</div>

<header class="hero" role="img" aria-label="Black and white photo of a rider in dressage attire on a horse">
  <div class="emblem"></div>
</header>
<div class="rule" style="top:262px"></div>
<h1 class="hero-title">CENTRAL IOWA'S PREMIER<br>DRESSAGE AND SPORT<br>HORSE TRAINING</h1>
<div class="rule" style="top:430px"></div>
<div class="hero-sub">LOCATED OUTSIDE DES MOINES, IOWA</div>
<div class="ph-note">IMAGE FOR PLACE HOLDER ONLY</div>
<div class="btn lg" style="left:499px;top:492px;width:202px">Signup Now</div>
<svg class="hero-curve" width="1200" height="140" viewBox="0 0 1200 140">
  <path d="M0,44 Q600,200 1200,44 L1200,140 L0,140 Z" fill="#262626"/>
  <path d="M0,44 Q600,200 1200,44" fill="none" stroke="#c9a27a" stroke-width="4"/>
</svg>

<!-- services -->
<h2 class="sec-title" style="left:189px;width:378px;top:630px">TRAINING</h2>
<h2 class="sec-title" style="left:633px;width:378px;top:630px">LESSONS</h2>
<div class="photo" style="left:189px;top:674px;width:378px;height:210px;background:linear-gradient(160deg,#8a8f6a,#5d6a45 55%,#6b5a48)" role="img" aria-label="Rider schooling a paint horse outside a barn"><div class="photo-label">FOR PLACE HOLDER ONLY</div></div>
<div class="photo" style="left:633px;top:674px;width:378px;height:210px;background:linear-gradient(160deg,#5c7a3e,#3d5a76 55%,#7a6a80)" role="img" aria-label="Two young riders in helmets beside a pony"><div class="photo-label">FOR PLACE HOLDER ONLY</div></div>
<p class="blurb" style="left:205px;top:899px;width:346px">Linden Ridge Stables offers both full and half time training options with Clara Whitfield. There is much flexibility with both rides and/or lessons weekly in the training packages...</p>
<p class="blurb" style="left:649px;top:899px;width:346px">Lessons are available for all ages of riders. Clara thoroughly enjoys working with accomplished riders looking to succeed in the show ring, as well as riders...</p>
<div class="btn" style="left:298px;top:985px;width:160px">Know More</div>
<div class="btn" style="left:741px;top:985px;width:160px">Read More</div>

<div class="dash" style="top:1057px"></div>

<!-- about -->
<h2 class="sec-head" style="top:1080px"><i></i>ABOUT US<i></i></h2>
<div class="photo" style="left:215px;top:1137px;width:329px;height:298px;border-radius:6px;background:linear-gradient(160deg,#d8d8dc,#8a7a6a 60%,#4a3a30)" role="img" aria-label="Rider performing dressage on a dark bay horse in an indoor arena"></div>
<p class="bio">International rider and trainer, Clara Whitfield began her riding career at a young age. She went up through the ranks of Junior Riders League and with an emphasis and focus in eventing. During college, Clara worked for a small breeder starting young horses. Clara loves starting young horses including starting and guiding them in a correct and quiet way to help them flourish. Her training focuses on gymnastic training incorporating ground work/lunging/long lining, jumping, cavelletti and regular hacking and trail riding. Clara is a NDL Silver Medalist having competed through the international levels of I1. A learner at heart, Clara regularly clinics and rides with other trainers and accomplished dressage riders from across the nation to continue to pursue her goal of competing at the Grand Prix. Clara has attended the NDL L Program as well as the Instructor/Trainer program to continue her growth as a trainer and rider. Clara trains and competes yearly in the winter season in Wellington, Florida to further her knowledge and development to share with her students!</p>
<div class="socials" style="left:550px;top:1453px" aria-label="Social links"><span></span><span></span><span></span></div>

<div class="dash" style="top:1523px"></div>

<!-- partnerships -->
<h2 class="sec-head" style="top:1546px"><i></i>PARTNERSHIPS<i></i></h2>
<div class="partner" style="left:197px">
  <div class="mark" style="color:#7a1c1c"><b style="background:#7a1c1c"></b>Meridian</div>
  <h3>Meridian Saddle Co.</h3>
  <p>Meridian Saddle Co. is constantly designing and researching saddles and riders to find the right blend of design and craftsmanship to fit today's demands. Every saddle's detail is carefully checked to be sure the workmanship and quality is there. All saddles are anatomically designed for horse and rider, hand-crafted from the finest leathers, and manufactured using the most technically advanced methods and features available.</p>
  <div class="btn" style="left:100px">Read More</div>
</div>
<div class="partner" style="left:609px">
  <div class="mark" style="color:#2f4a3a"><b style="background:#2f4a3a"></b>Harlow's</div>
  <h3>Harlow's Saddlery</h3>
  <p>My goal is to provide the best possible fit for both horse and rider whether it is a saddle you already own, one you have on trial, or one that I carry. Being a Qualified Saddle Fitter by the Guild of Saddle Fitters allows me to work with all saddle types and brands. In addition, I carry a broad range of saddles to fit your needs, both new and used. Having a multitude of saddles in my stock makes saddle shopping much easier for you.</p>
  <div class="btn" style="left:114px">Know More</div>
</div>

<div class="dash" style="top:2041px"></div>

<!-- faq -->
<h2 class="sec-head" style="top:2062px"><i></i>FREQUNETLY ASKED QUSETIONS<i></i></h2>
<div class="faq">
  <div class="q">Lorem ipsum dolor sit amet, consectetur adipiscing elit.<span class="tri"></span></div>
  <div class="q">Nam sodales, nulla quis condimentum aliquam, nunc justo vehicula ligula, et sagittis elit libero eget dui.<span class="tri up"></span></div>
  <div class="a">Proin malesuada felis orci, eget auctor nulla porttitor varius. Donec vestibulum bibendum turpis, ac iaculis dui tincidunt ut. Nulla sed turpis luctus, molestie dui ut, tincidunt tortor. Mauris vulputate fermentum blandit. Nullam faucibus accumsan odio, convallis dapibus eros blandit ut. Ut non eros et leo ultricies pellentesque. Phasellus lacinia massa non eros et scelerisque semper.</div>
  <div class="q">Praesent vel iaculis enim. Donec eget ornare sem. Donec pulvinar orci ipsum, non tempor nunc sagittis at.<span class="tri"></span></div>
  <div class="q">Vivamus convallis eleifend tortor, quis scelerisque metus vehicula nec.<span class="tri"></span></div>
  <div class="q">Donec in dolor cursus, blandit purus eget, fringilla purus. Nullam blandit vel risus at ultricies.<span class="tri"></span></div>
  <div class="q">Proin ipsum libero, varius ut fringilla at, dignissim id urna.<span class="tri"></span></div>
  <div class="q">Vivamus sed massa dignissim, dictum metus ut, mattis nibh.<span class="tri"></span></div>
  <div class="q">Praesent vel iaculis enim. Donec eget ornare sem. Donec pulvinar orci ipsum, non tempor nunc sagittis at.<span class="tri"></span></div>
  <div class="q">Vivamus convallis eleifend tortor, quis scelerisque metus vehicula nec.<span class="tri"></span></div>
  <div class="q">Donec in dolor cursus, blandit purus eget, fringilla purus. Nullam blandit vel risus at ultricies.<span class="tri"></span></div>
  <div class="q">Proin ipsum libero, varius ut fringilla at, dignissim id urna.<span class="tri"></span></div>
  <div class="q" style="border-bottom:1px solid var(--line)">Vivamus sed massa dignissim, dictum metus ut, mattis nibh.<span class="tri"></span></div>
</div>
<div class="more">CLICK FOR MORE</div>
<div class="dash" style="top:2654px"></div>

<div class="map" role="img" aria-label="Road map of the Des Moines, Iowa area"></div>

<footer class="footer">
  <div class="contact-h">CONTACT ME</div>
  <p class="contact-t">IF YOU ARE INTERESTED IN LEARNING MORE ABOUT LINDEN RIDGE STABLES' SERVICES OR AVAILABILITY FOR TRAINING OR LESSONS, PLEASE CONTACT US BELOW!</p>
  <div class="phone"><b>T:</b> 515-555-0187</div>
  <div class="socials" style="left:844px;top:128px" aria-label="Social links"><span></span><span></span><span></span></div>
  <div class="copy">© 2021 LINDEN RIDGE STABLES ALL RIGHTS RESERVED.</div>
</footer>

</body>
</html>
```